Stationery Design for Bright Harbor Supply LLC

Wholesalers of commercial & consumer products which sells the electronic products to tech savvy customers such as Hi-Tech, Software, CEO's, Entrepreneurs, Software Engineers, Software Management, Educational Institutions.

```html
<!DOCTYPE html>
<html lang="en">
<head>
<meta charset="utf-8">
<title>Bright Harbor Supply LLC – Business Card</title>
<link rel="stylesheet" href="https://fonts.googleapis.com/css2?family=Montserrat:wght@600;700&family=Archivo:wght@500&display=swap">
<style>
  :root {
    --navy: #0d1a78;
    --sky: #0ea0e6;
    --card-edge: #6b6b6b;
    --stripe-light: #fbfbfb;
    --stripe-dark: #e6e6e6;
    --page: #ffffff;
    --label: #111111;
  }
  html, body {
    margin: 0;
    padding: 0;
    width: 720px;
    height: 1200px;
    overflow: hidden;
    background: var(--page);
  }
  .sheet {
    position: relative;
    width: 720px;
    height: 1200px;
  }
  .side-label {
    position: absolute;
    left: 0;
    width: 720px;
    margin: 0;
    font-family: "Archivo", Arial, sans-serif;
    font-weight: 500;
    font-size: 30px;
    color: var(--label);
    letter-spacing: 0.5px;
  }
  .side-label--front { top: 2px; text-align: center; transform: translateX(-14px); }
  .side-label--back { top: 543px; text-align: center; transform: translateX(-32px); }

  .card {
    position: absolute;
    left: 3px;
    width: 712px;
    height: 430px;
    border: 2px solid var(--card-edge);
    border-radius: 3px;
    background: repeating-linear-gradient(
      to bottom,
      var(--stripe-light) 0px,
      var(--stripe-light) 10px,
      var(--stripe-dark) 10px,
      var(--stripe-dark) 19px
    );
    box-shadow: inset 0 0 10px rgba(0, 0, 0, 0.28);
    overflow: hidden;
    font-family: "Montserrat", Arial, sans-serif;
  }
  .card--front { top: 53px; }
  .card--back { top: 611px; }

  .contact {
    position: absolute;
    left: 20px;
    top: 160px;
    width: 240px;
    text-align: center;
    font-weight: 600;
    color: var(--sky);
  }
  .contact p { margin: 0; }
  .contact__name { font-size: 27px; font-weight: 700; color: var(--navy); line-height: 34px; }
  .contact__role { font-size: 21px; line-height: 36px; }
  .contact__phone { font-size: 21px; line-height: 34px; }
  .contact__email { font-size: 20px; line-height: 34px; }

  .arc {
    position: absolute;
    left: 236px;
    top: 68px;
    width: 130px;
    height: 236px;
  }

  .company {
    position: absolute;
    margin: 0;
    text-align: center;
    font-weight: 700;
    color: var(--navy);
    line-height: 1.1;
  }
  .company--front { left: 330px; top: 95px; width: 360px; font-size: 40px; }
  .company--back { left: 86px; top: 128px; width: 530px; font-size: 58px; }

  .rule {
    position: absolute;
    left: 0;
    top: 356px;
    width: 100%;
    height: 3px;
    background: var(--sky);
  }
  .address {
    position: absolute;
    left: 0;
    top: 380px;
    width: 644px;
    margin: 0;
    text-align: center;
    font-weight: 600;
    font-size: 22px;
    color: var(--sky);
  }
</style>
</head>
<body>
<main class="sheet">
  <h2 class="side-label side-label--front">Front Side</h2>
  <section class="card card--front">
    <div class="contact">
      <p class="contact__name">Name</p>
      <p class="contact__role">Manager</p>
      <p class="contact__phone">999999999</p>
      <p class="contact__email">xxxxxx@xxxx.ccc</p>
    </div>
    <svg class="arc" viewBox="0 0 130 236" aria-hidden="true">
      <path d="M6 6 A112 112 0 0 1 6 230" fill="none" stroke="var(--sky)" stroke-width="14"/>
    </svg>
    <p class="company company--front">Bright Harbor<br>Supply LLC</p>
    <div class="rule"></div>
    <p class="address">Address</p>
  </section>

  <h2 class="side-label side-label--back">Back Side</h2>
  <section class="card card--back">
    <p class="company company--back">Bright Harbor<br>Supply LLC</p>
  </section>
</main>
</body>
</html>
```